Takeaway coffee cup design for a trending coffee shop in soho London

We need a background design similar to the image attached "image 1". with BRUMLA PEWTIN written as our logo in Veneer. attached also is our current cup "image 2" if it helps to capture our use of colours.
Hex Codes: YELLOW: #FFF0AD (BRUMLA Colour)
Green: #1E3226 (Back ground colour)
Orange: #FF803D (S & H Colour)

```html
<!DOCTYPE html>
<html lang="en">
<head>
<meta charset="UTF-8">
<title>BRUMLA PEWTIN – Cup Wrap</title>
<link href="https://fonts.googleapis.com/css2?family=Bebas+Neue&display=swap" rel="stylesheet">
<style>
  :root {
    --canvas: #cbcbcb;
    --green: #1e3226;
    --green-leaf: #243a2d;
    --yellow: #fff0ad;
    --orange: #ff803d;
  }
  * { margin: 0; padding: 0; box-sizing: border-box; }
  html, body {
    width: 1200px;
    height: 1200px;
    overflow: hidden;
    background: var(--canvas);
  }
  .stage {
    position: relative;
    width: 1200px;
    height: 1200px;
  }
  .cup-wrap {
    position: absolute;
    left: 83px;
    top: 116px;
    width: 1035px;
    height: 430px;
    display: block;
  }
  .wrap-ground { fill: var(--green); }
  .band-thick { fill: none; stroke: var(--yellow); stroke-width: 22; }
  .band-accent { fill: none; stroke: var(--orange); stroke-width: 7; }
  .band-thin { fill: none; stroke: var(--yellow); stroke-width: 5; }
  .brand-name,
  .brand-place {
    font-family: "Bebas Neue", "Oswald", sans-serif;
    fill: var(--yellow);
    text-anchor: middle;
  }
  .brand-name { font-size: 138px; letter-spacing: 2px; }
  .brand-place { font-size: 120px; letter-spacing: 3px; }
</style>
</head>
<body>
<main class="stage">
  <svg class="cup-wrap" viewBox="0 0 1667 692" preserveAspectRatio="none" aria-labelledby="wrap-title">
    <title id="wrap-title">BRUMLA PEWTIN takeaway cup wrap</title>
    <defs>
      <radialGradient id="leaf-tone" cx="50%" cy="50%" r="70%">
        <stop offset="0" stop-color="#223829"/>
        <stop offset="1" stop-color="#1e3226"/>
      </radialGradient>
    </defs>

    <rect class="wrap-ground" x="0" y="0" width="1667" height="692"/>
    <rect class="leaf-pattern" x="0" y="0" width="1667" height="692" fill="url(#leaf-tone)"
          role="img" aria-label="Faint tonal pattern of leafy sprigs covering the wrap"/>

    <g class="wave wave-top">
      <path class="band-thick" d="M0,78 C400,132 700,92 1000,62 S1480,34 1667,74"/>
      <path class="band-accent" d="M0,106 C400,156 700,116 1000,88 S1480,66 1667,104"/>
      <path class="band-thin" d="M0,122 C400,172 700,132 1000,104 S1480,84 1667,121"/>
    </g>

    <g class="wave wave-bottom">
      <path class="band-thick" d="M0,578 C300,532 700,552 1000,588 S1480,630 1667,580"/>
      <path class="band-accent" d="M0,604 C300,560 700,578 1000,612 S1480,650 1667,606"/>
      <path class="band-thin" d="M0,619 C300,576 700,594 1000,628 S1480,666 1667,621"/>
    </g>

    <g class="brand-lockup brand-lockup--left">
      <text class="brand-name" x="400" y="330">BRUMLA</text>
      <text class="brand-place" x="400" y="462">PEWTIN</text>
    </g>

    <g class="brand-lockup brand-lockup--right">
      <text class="brand-name" x="1268" y="330">BRUMLA</text>
      <text class="brand-place" x="1268" y="462">PEWTIN</text>
    </g>
  </svg>
</main>
</body>
</html>
```